Content developers BC and Stationary
Nubra نبراس
Content developers BC and Stationary - Corporate Services
Creative Brief
Simple
Rana T alMuttairi
Creative Director
Jeddah
rana@nubraco.com
for second partner, with Arabic on the back: Khaled Naji خالد ناجي Managing Director المدير التنفيذي +966507213690 +٩٦٦٥٠٧٢١٣٦٩٠ k@nubraco.com
رنا طارق المطيري المدير الإبداعي +٩٦٦٥٠٨٤٤١٢٥٩ rana@nubraco.com
Concepts
Business Cards and Stationery for new compliance company.
Business Cards and Stationery for Background Check Company

```html
<!DOCTYPE html>
<html lang="en">
<head>
<meta charset="utf-8">
<title>Nubra — Business Card</title>
<link href="https://fonts.googleapis.com/css2?family=Montserrat:wght@400;600;700&display=swap" rel="stylesheet">
<style>
  :root {
    --bg: #e9e9ec;
    --card: #ffffff;
    --purple: #8b5fb6;
    --indigo: #3a3c9c;
    --ink-light: #ffffff;
    --shadow: rgba(0, 0, 0, 0.18);
  }
  * { box-sizing: border-box; margin: 0; padding: 0; }
  html, body {
    width: 1200px;
    height: 901px;
    overflow: hidden;
    background: var(--bg);
    font-family: "Montserrat", Arial, sans-serif;
  }
  .stage {
    width: 1200px;
    height: 901px;
    display: flex;
    align-items: center;
    justify-content: center;
    gap: 50px;
  }
  .card {
    position: relative;
    width: 540px;
    height: 310px;
    background: var(--card);
    border-radius: 14px;
    box-shadow: 0 10px 30px var(--shadow);
    overflow: hidden;
  }
  .brand {
    display: flex;
    align-items: center;
    gap: 10px;
    color: var(--purple);
    font-weight: 700;
    letter-spacing: 1px;
  }
  .brand-mark {
    width: 14px;
    height: 14px;
    background: var(--indigo);
  }
  .card-front .brand {
    position: absolute;
    left: 50%;
    top: 50%;
    transform: translate(-50%, -50%);
    font-size: 52px;
  }
  .card-back .backdrop {
    position: absolute;
    inset: 0;
  }
  .card-back .brand {
    position: absolute;
    left: 38px;
    top: 120px;
    font-size: 40px;
  }
  .contact {
    position: absolute;
    right: 26px;
    top: 30px;
    text-align: right;
    color: var(--ink-light);
    font-size: 11px;
    line-height: 1.35;
  }
  .contact-name {
    font-size: 13px;
    font-weight: 600;
    text-transform: uppercase;
    letter-spacing: 0.5px;
  }
  .contact-title {
    font-size: 9px;
    text-transform: uppercase;
    letter-spacing: 1px;
    margin-bottom: 22px;
  }
  .contact-address { margin-bottom: 20px; }
  .contact-line {
    display: flex;
    justify-content: flex-end;
    align-items: center;
    gap: 8px;
    margin-bottom: 6px;
  }
  .contact-line svg {
    width: 10px;
    height: 10px;
    fill: none;
    stroke: var(--ink-light);
    stroke-width: 1.4;
  }
  .contact-gap { margin-top: 12px; }
</style>
</head>
<body>
<main class="stage">
  <section class="card card-front" aria-label="Card front">
    <div class="brand"><span class="brand-mark"></span>Nubra</div>
  </section>

  <section class="card card-back" aria-label="Card back">
    <svg class="backdrop" viewBox="0 0 540 310" preserveAspectRatio="none">
      <path d="M290,0 Q200,150 240,310 L540,310 L540,0 Z" fill="var(--purple)"/>
      <path d="M278,0 Q186,150 228,310 L242,310 Q202,150 292,0 Z" fill="var(--indigo)"/>
    </svg>
    <div class="brand"><span class="brand-mark"></span>Nubra</div>
    <div class="contact">
      <p class="contact-name">Rana T alMuttairi</p>
      <p class="contact-title">Creative Director</p>
      <p class="contact-address">112, 9th floor, Tower<br>Corniche Road JED</p>
      <p class="contact-line">+966 50 721 3690
        <svg viewBox="0 0 10 10"><path d="M2 1 L4 1 L5 3 L4 4 Q5 6 6 6 L7 5 L9 6 L9 8 Q8 9 7 9 Q1 8 1 2 Q1 1 2 1 Z"/></svg>
      </p>
      <p class="contact-line">+966 50 721 3690
        <svg viewBox="0 0 10 10"><rect x="2.5" y="0.8" width="5" height="8.4" rx="1"/><line x1="4.5" y1="7.6" x2="5.5" y2="7.6"/></svg>
      </p>
      <p class="contact-line">+966 50 721 3690
        <svg viewBox="0 0 10 10"><rect x="1" y="3" width="8" height="5" rx="0.5"/><path d="M3 3 V1 H7 V3"/></svg>
      </p>
      <p class="contact-line contact-gap">rana@nubraco.com
        <svg viewBox="0 0 10 10"><rect x="0.8" y="2" width="8.4" height="6"/><path d="M0.8 2 L5 5.5 L9.2 2"/></svg>
      </p>
      <p class="contact-line">www.nubraco.com
        <svg viewBox="0 0 10 10"><circle cx="5" cy="5" r="4"/><path d="M1 5 H9 M5 1 Q2.5 5 5 9 M5 1 Q7.5 5 5 9"/></svg>
      </p>
    </div>
  </section>
</main>
</body>
</html>
```